Cedar Hall businesscard

We changed our name and logo, now we need new business cards.
3-4/71 Marlow Street Fernbrook 2190
www.cedarhallfellowship.example
info@cedarhallfellowship.example
Louise-Jane Tredwick
Senior Pastor
ph: 02 95558172

Industry/Entity Type

Business

```html
<!DOCTYPE html>
<html lang="en">
<head>
<meta charset="utf-8">
<title>Cedar Hall — Business Card</title>
<link href="https://fonts.googleapis.com/css2?family=Arimo:wght@400&display=swap" rel="stylesheet">
<style>
  :root {
    --canvas-bg: #e4e4e2;
    --card-bg: #ffffff;
    --ink: #1c1c1c;
    --accent: #6f8496;
    --accent-soft: #8fa0ae;
    --figure-dark: #2a2a2a;
    --figure-light: #c9c9c9;
  }
  * { margin: 0; padding: 0; box-sizing: border-box; }
  html, body {
    width: 1200px;
    height: 848px;
    overflow: hidden;
    background: var(--canvas-bg);
    font-family: "Arimo", Arial, sans-serif;
    color: var(--ink);
  }
  .business-card {
    position: absolute;
    left: 100px;
    top: 138px;
    width: 1000px;
    height: 572px;
    background: var(--card-bg);
    border-radius: 30px;
    box-shadow: 0 10px 30px rgba(0,0,0,0.12);
    overflow: hidden;
  }
  .identity {
    position: absolute;
    left: 64px;
    top: 52px;
  }
  .identity__name {
    font-size: 36px;
    font-weight: 400;
    letter-spacing: 0.2px;
  }
  .identity__title {
    font-size: 23px;
    margin-top: 4px;
  }
  .brand {
    position: absolute;
    right: 56px;
    top: 74px;
    display: flex;
    align-items: center;
    gap: 14px;
  }
  .brand__dot {
    width: 26px;
    height: 26px;
    border-radius: 50%;
    background: var(--accent-soft);
  }
  .brand__name {
    font-size: 34px;
    font-weight: 400;
    color: var(--accent);
    letter-spacing: 1px;
  }
  .contact-list {
    position: absolute;
    left: 64px;
    top: 330px;
    list-style: none;
  }
  .contact-list__item {
    display: flex;
    align-items: center;
    gap: 16px;
    font-size: 26px;
    line-height: 40px;
    white-space: nowrap;
  }
  .contact-list__icon {
    width: 20px;
    height: 20px;
    flex: none;
  }
  .contact-list__highlight { color: var(--accent); }
  .family-figures {
    position: absolute;
    right: 50px;
    bottom: 0;
    width: 340px;
    height: 290px;
    border-radius: 130px 130px 0 0;
    background: linear-gradient(90deg, var(--figure-light) 0%, var(--figure-dark) 45%, var(--figure-dark) 75%, var(--figure-light) 100%);
    opacity: 0.85;
  }
</style>
</head>
<body>
  <article class="business-card">
    <header class="identity">
      <h1 class="identity__name">Louise-Jane Tredwick</h1>
      <p class="identity__title">Senior Pastor</p>
    </header>

    <div class="brand">
      <span class="brand__dot"></span>
      <span class="brand__name">Cedar Hall</span>
    </div>

    <ul class="contact-list">
      <li class="contact-list__item">
        <svg class="contact-list__icon" viewBox="0 0 20 20" aria-hidden="true">
          <path d="M4 2 L8 2 L9 6 L7 8 C8 11 9 12 12 13 L14 11 L18 12 L18 16 C18 17 17 18 16 18 C8 18 2 12 2 4 C2 3 3 2 4 2 Z" fill="var(--ink)"/>
        </svg>
        <span>02 95558172</span>
      </li>
      <li class="contact-list__item">
        <svg class="contact-list__icon" viewBox="0 0 20 20" aria-hidden="true">
          <circle cx="10" cy="10" r="8.5" fill="none" stroke="var(--ink)" stroke-width="2"/>
          <ellipse cx="10" cy="10" rx="3.5" ry="8.5" fill="none" stroke="var(--ink)" stroke-width="1.6"/>
          <line x1="2" y1="10" x2="18" y2="10" stroke="var(--ink)" stroke-width="1.6"/>
        </svg>
        <span>www.<span class="contact-list__highlight">cedarhall</span>fellowship.example</span>
      </li>
      <li class="contact-list__item">
        <svg class="contact-list__icon" viewBox="0 0 20 20" aria-hidden="true">
          <rect x="1.5" y="4" width="17" height="12" fill="none" stroke="var(--ink)" stroke-width="2"/>
          <path d="M1.5 4 L10 11 L18.5 4" fill="none" stroke="var(--ink)" stroke-width="2"/>
        </svg>
        <span>info@<span class="contact-list__highlight">cedarhall</span>fellowship.example</span>
      </li>
      <li class="contact-list__item">
        <svg class="contact-list__icon" viewBox="0 0 20 20" aria-hidden="true">
          <path d="M10 1 C6 1 3.5 4 3.5 7.5 C3.5 12 10 19 10 19 C10 19 16.5 12 16.5 7.5 C16.5 4 14 1 10 1 Z" fill="var(--ink)"/>
          <circle cx="10" cy="7.5" r="2.5" fill="var(--card-bg)"/>
        </svg>
        <span>3-4/71 Marlow Street Fernbrook 2190</span>
      </li>
    </ul>

    <div class="family-figures" role="img" aria-label="Silhouette of a family walking hand in hand, with faded grey figures behind"></div>
  </article>
</body>
</html>
```